依頼詳細
国家資格に対応するための新規講習の開講を予定しまして新しいチラシを作成したいと思っております。
令和5年5月リリース予定の新規講習に関しましての広告及び講習に関する説明を行えるチラシのデザインをお願いいたします。
令和5年5月リリース予定ですが、既存の講習受講後に新規講習を追加で受ける形の受講も可能であるため、それまでの間の従来の講習も広告も行っていきたいと思っております。
従来の講習→新規講習の受講の流れを勧めたいです。

利用用途は新聞折込及び、ポスティングにて利用いたします。
希望はA4片面カラーを希望いたします。

納品はpsdファイルおよびPDFファイル(プリモアにすぐに入稿できる仕様)を希望いたします。
記載項目
■校名
ドローン教習所 翠光小樽校・道央MTR校
■空撮技能認定ロゴ

```html
<!DOCTYPE html>
<html lang="ja">
<head>
<meta charset="utf-8">
<title>ドローン国家資格コース開講 受講者募集</title>
<link href="https://fonts.googleapis.com/css2?family=Noto+Sans+JP:wght@400;700;900&family=Noto+Serif+JP:wght@700;900&display=swap" rel="stylesheet">
<style>
:root{
  --navy:#0d2a5c;
  --navy-deep:#081c40;
  --sky-top:#1b3f7a;
  --sky-mid:#4f86c4;
  --sky-low:#c9dff2;
  --yellow:#ffe000;
  --orange:#f08a00;
  --blue:#1f6fc0;
  --white:#ffffff;
  --ink:#1a2a48;
}
*{margin:0;padding:0;box-sizing:border-box}
html,body{width:846px;height:1200px;overflow:hidden;background:var(--white)}
body{font-family:"Noto Sans JP",sans-serif;color:var(--ink)}
.flyer{position:relative;width:846px;height:1200px;overflow:hidden;background:linear-gradient(180deg,#eef5fc 0%,#ffffff 70%)}
.hero-photo{position:absolute;left:0;top:0;width:846px;height:720px;
  background:linear-gradient(180deg,var(--sky-top) 0%,#2d5d9c 30%,var(--sky-mid) 55%,#8fb6de 80%,var(--sky-low) 100%)}
.release-badge{position:absolute;left:140px;top:148px;width:290px;height:56px;background:var(--navy);
  transform:skewX(-14deg);display:flex;align-items:center;justify-content:center;border-radius:4px}
.release-badge span{transform:skewX(14deg);color:var(--white);font-weight:900;font-size:36px;letter-spacing:2px;font-style:italic}
.headline{position:absolute;font-family:"Noto Serif JP",serif;font-weight:900;line-height:1;
  text-shadow:0 4px 8px rgba(0,20,60,.55)}
.headline.drone{left:150px;top:218px;font-size:88px;color:var(--white)}
.headline.license{left:56px;top:310px;font-size:128px;color:var(--yellow);letter-spacing:2px}
.headline.recruit{left:36px;top:440px;font-size:124px;color:var(--white)}
.course-open{position:absolute;left:560px;top:180px;transform:rotate(-18deg);font-family:"Noto Serif JP",serif;
  font-weight:900;color:var(--yellow);font-size:72px;line-height:1.05;text-align:right;text-shadow:0 4px 8px rgba(0,20,60,.55)}
.mlit-strip{position:absolute;left:440px;top:594px;width:406px;height:40px;
  background:linear-gradient(90deg,rgba(13,42,92,0) 0%,var(--navy) 25%,var(--navy) 100%);
  color:var(--white);font-weight:700;font-size:19px;display:flex;align-items:center;justify-content:flex-end;padding-right:18px;font-style:italic}
.mlit-strip b{color:var(--yellow)}
.training-photo{position:absolute;left:20px;top:652px;width:430px;height:124px;border-radius:4px;
  background:linear-gradient(180deg,#9cc3e6 0%,#cfe0ee 55%,#8fa86a 100%)}
.lead{position:absolute;left:24px;top:790px;width:430px;font-weight:900;font-size:24px;line-height:1.5;color:var(--navy)}
.lead em{font-style:normal;color:var(--orange);font-size:30px}
.course-card{position:absolute;top:880px;width:200px;height:180px;border:3px solid;background:var(--white)}
.course-card h3{color:var(--white);font-size:24px;font-weight:900;text-align:center;padding:6px 0;line-height:1.2}
.course-card h3 small{display:block;font-size:13px;font-weight:700}
.course-card.basic{left:20px;border-color:var(--orange)}
.course-card.basic h3{background:var(--orange)}
.course-card.exam{left:250px;border-color:var(--blue)}
.course-card.exam h3{background:var(--blue)}
.course-card p{font-size:14px;font-weight:700;line-height:1.5;padding:8px 10px 0}
.course-card .label{display:inline-block;background:var(--navy);color:var(--white);font-size:13px;padding:1px 8px;margin:10px 0 0 10px}
.price{position:absolute;bottom:8px;left:0;right:0;text-align:center;font-weight:900;font-size:34px;color:#d42a1a;line-height:1}
.price small{font-size:14px;color:var(--ink)}
.flow-arrow{position:absolute;left:222px;top:950px}
.info-panel{position:absolute;left:470px;top:648px;width:360px;height:318px;background:var(--navy);padding:16px 18px;color:var(--white)}
.info-panel h2{display:inline-block;border:2px solid var(--white);font-size:22px;font-weight:900;padding:2px 12px;margin-bottom:8px}
.info-panel p{font-size:13px;line-height:1.7;margin-bottom:12px}
.brand{position:absolute;left:580px;top:995px;display:flex;align-items:center;gap:12px}
.brand .mark{width:46px;height:46px;border-radius:50%;background:var(--blue)}
.brand .name{font-weight:900;font-size:30px;color:var(--navy)}
.footer{position:absolute;left:0;top:1086px;width:846px;height:114px;background:var(--navy-deep);color:var(--white);padding:16px 28px;display:flex;justify-content:space-between;align-items:center}
.footer .school{font-size:20px;font-weight:700;line-height:1.5}
.footer .tel{font-size:40px;font-weight:900;letter-spacing:1px}
.footer .tel small{font-size:24px}
.footer .web{font-size:14px;line-height:1.8;text-align:right}
</style>
</head>
<body>
<main class="flyer">
  <div class="hero-photo" role="img" aria-label="海と空を背景に飛行するドローンの写真"></div>

  <div class="release-badge"><span>2023年 5月</span></div>
  <h1 class="headline drone">ドローン</h1>
  <div class="headline license">国家資格</div>
  <div class="course-open">コース<br>開講</div>
  <div class="headline recruit">受講者募集!</div>

  <div class="mlit-strip"><span>ドローン<b>国家資格</b>は国土交通省認定です</span></div>

  <div class="training-photo" role="img" aria-label="屋外でドローン操縦を練習する講習風景の写真"></div>

  <p class="lead">まずは<em>基礎技能講習</em>から始め、<br>次に<em>国家試験コース</em>を受講しよう!</p>

  <section class="course-card basic">
    <h3>基礎技能講習</h3>
    <p>取得可能ライセンス<br>1)空撮技能認定3級<br>2)基礎技能ライセンス<br>(空撮技能認定公認)</p>
    <div class="price">99,000<small>円(税込)</small></div>
  </section>

  <svg class="flow-arrow" width="28" height="44" viewBox="0 0 28 44" aria-hidden="true">
    <polygon points="0,0 28,22 0,44" fill="#1f6fc0"/>
  </svg>

  <section class="course-card exam">
    <h3>国家試験講習<small>(基礎技能講習受講者)</small></h3>
    <span class="label">講習内容</span>
    <div class="price">112,200<small>円(税込)</small></div>
  </section>

  <aside class="info-panel">
    <h2>国家試験コースとは</h2>
    <p>基礎技能講習を修了した方が、国家資格である無人航空機操縦者技能証明の取得を目指すコースです。学科と実技の試験対策を、経験豊富な講師が丁寧に指導します。</p>
    <h2>内容</h2>
    <p>学科講習と実技講習を組み合わせ、法令や安全運航の知識から目視外飛行までを段階的に学びます。修了後は指定試験機関での受験に進めます。</p>
  </aside>

  <div class="brand">
    <span class="mark" aria-hidden="true"></span>
    <span class="name">空撮技能認定</span>
  </div>

  <footer class="footer">
    <div>
      <div class="school">ドローン教習所<br>翠光小樽校・道央MTR校</div>
    </div>
    <div class="tel"><small>TEL:</small>0134-00-5821</div>
    <div class="web">info@suiko-sky.jp<br>www.suiko-sky.jp/course/</div>
  </footer>
</main>
</body>
</html>
```